front store banner

i need a banner 4'x8' for a print shop store front promoting custom t-shirts, banners, sublimated mugs, business cards, car magnets, window decals, postcards and passport pictures

```html
<!DOCTYPE html>
<html lang="en">
<head>
<meta charset="utf-8">
<title>Custom Printing – Storefront Banner</title>
<link href="https://fonts.googleapis.com/css2?family=Bebas+Neue&family=Montserrat:wght@300&display=swap" rel="stylesheet">
<style>
  :root {
    --navy: #0b0f3e;
    --yellow: #fec200;
    --ink: #000000;
    --white: #ffffff;
    --porcelain-light: #f5f5f5;
    --porcelain-shade: #d9d9d9;
    --shirt-light: #ececec;
    --shirt-shade: #c9c9c9;
    --shirt-dark: #4b4b4b;
    --shirt-darker: #2f2f2f;
  }
  * { margin: 0; padding: 0; box-sizing: border-box; }
  html, body {
    width: 1200px;
    height: 1200px;
    overflow: hidden;
    background: var(--navy);
  }
  .sheet {
    position: relative;
    width: 1200px;
    height: 1200px;
    background: var(--navy);
  }
  .banner {
    position: absolute;
    left: 95px;
    width: 1017px;
    height: 527px;
    background: var(--yellow);
    overflow: hidden;
  }
  .banner--top { top: 48px; }
  .banner--bottom { top: 606px; }

  .product-art { position: absolute; }
  .product-art--cards {
    left: 0; top: 0; width: 125px; height: 330px;
    border-radius: 0 0 18px 0;
    background: linear-gradient(135deg, var(--porcelain-light), var(--porcelain-shade));
  }
  .product-art--mug-left {
    left: 0; top: 345px; width: 185px; height: 182px;
    border-radius: 0 18px 0 0;
    background: linear-gradient(90deg, var(--porcelain-shade), var(--porcelain-light));
  }
  .product-art--mug-right {
    left: 190px; top: 388px; width: 220px; height: 139px;
    border-radius: 10px 40px 0 0;
    background: linear-gradient(90deg, var(--porcelain-light), var(--porcelain-shade));
  }
  .product-art--shirt-white {
    left: 905px; top: 10px; width: 112px; height: 350px;
    border-radius: 40px 0 0 0;
    background: linear-gradient(180deg, var(--shirt-light), var(--shirt-shade));
  }
  .product-art--shirt-dark {
    left: 780px; top: 345px; width: 237px; height: 182px;
    border-radius: 60px 0 0 0;
    background: linear-gradient(180deg, var(--shirt-dark), var(--shirt-darker));
  }

  .headline-block {
    position: absolute;
    inset: 0;
    text-align: center;
    color: var(--ink);
  }
  .open-now__bar {
    position: absolute;
    left: 323px; top: 110px;
    width: 368px; height: 11px;
    background: var(--white);
  }
  .open-now {
    position: absolute;
    left: 0; right: 0; top: 78px;
    font-family: "Montserrat", sans-serif;
    font-weight: 300;
    font-size: 45px;
    line-height: 1;
    letter-spacing: 0.27em;
    padding-left: 0.27em;
  }
  .title {
    position: absolute;
    left: 0; right: 0; top: 139px;
    font-family: "Bebas Neue", sans-serif;
    font-weight: 400;
    font-size: 105px;
    line-height: 1;
  }
  .service-line {
    position: absolute;
    left: 0; right: 0;
    font-family: "Bebas Neue", sans-serif;
    font-weight: 400;
    font-size: 47px;
    line-height: 1;
    white-space: nowrap;
  }
  .service-line__sep { margin: 0 0.18em; }
  .service-line--one { top: 238px; }
  .service-line--two { top: 291px; }
  .service-line--three { top: 343px; }
</style>
</head>
<body>
<main class="sheet">
  <section class="banner banner--top">
    <div class="product-art product-art--cards" role="img" aria-label="Photo of stacked blank white business cards"></div>
    <div class="product-art product-art--mug-left" role="img" aria-label="Photo of a tilted white ceramic mug"></div>
    <div class="product-art product-art--mug-right" role="img" aria-label="Photo of an upright white ceramic mug"></div>
    <div class="product-art product-art--shirt-white" role="img" aria-label="Photo of a white t-shirt"></div>
    <div class="product-art product-art--shirt-dark" role="img" aria-label="Photo of a charcoal t-shirt"></div>
    <div class="headline-block">
      <div class="open-now__bar"></div>
      <p class="open-now">OPEN NOW</p>
      <h1 class="title">CUSTOM PRINTING</h1>
      <p class="service-line service-line--one">T-SHIRT<span class="service-line__sep">|</span>BANNERS<span class="service-line__sep">|</span>MUGS<span class="service-line__sep">|</span>BUSSINES CARDS</p>
      <p class="service-line service-line--two">CAR MAGNETS<span class="service-line__sep">|</span>WINDOW DECALS<span class="service-line__sep">|</span>POSTCARDS</p>
      <p class="service-line service-line--three">PASSPORT PICTURES</p>
    </div>
  </section>

  <section class="banner banner--bottom">
    <div class="product-art product-art--cards" role="img" aria-label="Photo of stacked blank white business cards"></div>
    <div class="product-art product-art--mug-left" role="img" aria-label="Photo of a tilted white ceramic mug"></div>
    <div class="product-art product-art--mug-right" role="img" aria-label="Photo of an upright white ceramic mug"></div>
    <div class="product-art product-art--shirt-white" role="img" aria-label="Photo of a white t-shirt"></div>
    <div class="product-art product-art--shirt-dark" role="img" aria-label="Photo of a charcoal t-shirt"></div>
    <div class="headline-block">
      <div class="open-now__bar"></div>
      <p class="open-now">OPEN NOW</p>
      <h2 class="title">CUSTOM PRINTING</h2>
      <p class="service-line service-line--one">T-SHIRT<span class="service-line__sep">|</span>BANNERS<span class="service-line__sep">|</span>MUGS<span class="service-line__sep">|</span>BUSSINES CARDS</p>
      <p class="service-line service-line--two">CAR MAGNETS<span class="service-line__sep">|</span>WINDOW DECALS<span class="service-line__sep">|</span>POSTCARDS</p>
      <p class="service-line service-line--three">PASSPORT PICTURES</p>
    </div>
  </section>
</main>
</body>
</html>
```